Webdesign für Kleingruppenreisen in die Südsteiermark
Zielgruppe
Wir sind ein Start-Up Unternehmen, das als Kleingruppenreisen in die Südsteiermark veranstaltet; der Schwerpunkt liegt auf dem Kulinarischen. Zielgruppe sind Geschäftsleute, die diese Kurzreisen (Do-So) für Marketingzwecke oder als Mitarbeiterbonus (oder auch privat) nutzen möchten.
Aufgabenstellung
Die Homepage soll eine Online-Shop Möglichkeit bieten, in der die Reise (bisher gibt es nur einen Ablauf) gebucht werden kann. Optisch sollte sie sich an das bereits von Ihnen erstellte Logo anlehnen und möglichst ansprechende Fotos von der Südsteiermark, Graz, Leoben usw. enthalten. (Siehe die beiden Flyer und das Logo)
Wir haben inzwischen Bildfreigaben von Mirtler und dem Tourismusverband Hollerau erhalten und können auch eigene Bilder zur Verfügung stellen. Bitte kontaktieren Sie uns dafür, wenn nötig.

```html
<!DOCTYPE html>
<html lang="de">
<head>
<meta charset="utf-8">
<title>Gaumenwege – Kleingruppenreisen in die Südsteiermark</title>
<link href="https://fonts.googleapis.com/css2?family=Open+Sans:ital,wght@0,300;0,400;0,600;1,400;1,600&family=Yellowtail&display=swap" rel="stylesheet">
<style>
:root{
  --green:#23603b;
  --green-nav:#2d6f46;
  --green-deep:#1f5634;
  --text:#333;
  --nav-grey:#5a5a5a;
  --panel-grey:#e6e6e6;
  --btn-grey:#717171;
  --white:#fff;
}
*{margin:0;padding:0;box-sizing:border-box}
html,body{width:1200px;height:2178px;overflow:hidden;background:var(--white)}
body{position:relative;font-family:"Open Sans",sans-serif;color:var(--text)}
.abs{position:absolute}
.script{font-family:"Yellowtail",cursive;font-weight:400}

.top-bar{left:0;top:0;width:1200px;height:37px;background:var(--green)}
.site-header{left:0;top:37px;width:1200px;height:135px;background:var(--white);box-shadow:0 2px 3px rgba(0,0,0,.15);z-index:2}
.brand{left:96px;top:86px;display:flex;align-items:center;gap:10px;font-size:26px;font-weight:600;color:var(--green);z-index:3}
.brand-dot{width:34px;height:34px;border-radius:50%;background:var(--green)}
.main-nav{left:460px;top:94px;display:flex;gap:20px;font-size:16px;color:var(--nav-grey);z-index:3}
.main-nav .active{color:var(--green-nav)}
.search-icon{left:944px;top:92px;z-index:3}

.hero{left:0;top:172px;width:1200px;height:452px;background:linear-gradient(90deg,#3f7f46 0%,#5f8d6a 40%,#6a9171 55%,#3e7d3e 100%)}
.hero-title{left:0;top:348px;width:1200px;text-align:center;color:var(--white);font-size:42px;line-height:52px}
.hero-sub{left:0;top:395px;width:1200px;text-align:center;color:var(--white);font-size:30px;font-weight:300}
.hero-btn{left:479px;top:482px;width:241px;height:53px;border:2px solid var(--white);color:var(--white);font-size:19px;display:flex;align-items:center;justify-content:center}

.welcome{left:0;top:624px;width:1200px;height:406px;background:linear-gradient(90deg,#fff 0%,#fff 45%,#f1f0ee 100%)}
.welcome-art{left:820px;top:630px;width:380px;height:396px;background:radial-gradient(ellipse at 55% 50%,#c9a46a 0%,#9fb85a 40%,rgba(241,240,238,0) 72%)}
.welcome-title{left:105px;top:670px;font-size:29px;color:#444}
.welcome-text{left:105px;top:721px;width:640px;font-size:12.6px;line-height:15px;color:#222}
.welcome-text p+p{margin-top:15px}
.more-btn{left:105px;top:933px;width:181px;height:44px;border:1px solid #999;font-size:22px;color:#444;display:flex;align-items:center;justify-content:center}

.offers{left:0;top:1030px;width:1200px;height:478px;background:var(--panel-grey)}
.feature{left:106px;top:1058px;width:375px;height:374px;background:linear-gradient(160deg,#7a9a55 0%,#8a8460 50%,#6b4e34 100%)}
.feature-title{left:106px;top:1268px;width:367px;text-align:right;color:var(--white);font-size:32px;line-height:38px}
.feature-sub{left:106px;top:1308px;width:367px;text-align:right;color:var(--white);font-size:14px;font-weight:600;line-height:18px}
.feature-btn{left:342px;top:1363px;width:125px;height:31px;background:rgba(255,255,255,.75);font-style:italic;font-size:15px;color:#222;display:flex;align-items:center;justify-content:center}

.card-img{top:1058px;width:175px;height:174px}
.img-vine{background:linear-gradient(160deg,#4b7a2e,#8fb35a 60%,#d9dccf)}
.img-town{background:linear-gradient(180deg,#8fb0cc,#c86a3a 45%,#b5532d 80%,#7a7f85)}
.img-lake{background:linear-gradient(180deg,#9fc0dc 0%,#5f7e4e 35%,#3a86b0 65%,#c9dce0 100%)}
.card-title{top:1256px;font-size:16px;line-height:18px;color:var(--green)}
.card-text{top:1276px;font-size:11.5px;line-height:13px;color:#222}
.card-price{top:1316px;font-size:19px;color:var(--green)}
.card-btn{top:1388px;width:175px;height:43px;background:var(--btn-grey);color:var(--white);font-style:italic;font-size:16px;display:flex;align-items:center;justify-content:center}
.slider-dot{top:1467px;width:9px;height:9px;border-radius:50%;background:#c6c6c6}
.slider-dot.on{background:#111}
.arrow{top:1462px}

.cta{left:0;top:1508px;width:1200px;height:295px;background:linear-gradient(120deg,#4f7e55 0%,#5f8a68 45%,#3f7046 100%)}
.cta-title{left:228px;top:1545px;color:var(--white);font-size:29px;font-weight:600;font-style:italic;line-height:36px}
.cta-sub{left:228px;top:1655px;color:var(--white);font-size:22px;font-weight:300;line-height:27px}
.cta-btn{left:692px;top:1701px;width:287px;height:43px;border:1px solid var(--white);color:var(--white);font-style:italic;font-size:22px;display:flex;align-items:center;justify-content:center}

.hills{left:0;top:1840px;width:560px;height:134px}
.footer{left:0;top:1973px;width:1200px;height:205px;background:var(--green)}
.f-text{color:var(--white)}
.f-name{left:250px;top:2004px;font-size:14px;font-weight:600;line-height:18px}
.f-addr{left:250px;top:2022px;font-size:11px;line-height:13.5px}
.f-phone{left:250px;top:2076px;font-size:11px;line-height:13.5px}
.f-icon{left:228px}
.f-col{top:2007px;font-size:11px;line-height:22px;letter-spacing:.3px}
.f-col strong{font-weight:600}
.social{top:2014px;width:51px;height:51px;border-radius:50%;background:var(--white)}
.f-rule{left:226px;top:2129px;width:751px;height:1px;background:rgba(255,255,255,.7)}
.copyright{left:0;top:2141px;width:1200px;text-align:center;font-size:11px;font-weight:300}
</style>
</head>
<body>

<div class="abs top-bar"></div>
<header class="abs site-header"></header>
<div class="abs brand"><span class="brand-dot"></span>Gaumenwege</div>
<nav class="abs main-nav">
  <span class="active">Home</span><span>Shop</span><span>Menüpunkt</span><span>Menüpunkt</span><span>Kontakt</span>
</nav>
<svg class="abs search-icon" width="28" height="28" viewBox="0 0 28 28" aria-label="Suche">
  <circle cx="17" cy="11" r="8" fill="none" stroke="#111" stroke-width="3"/>
  <line x1="11" y1="17" x2="3" y2="25" stroke="#111" stroke-width="4" stroke-linecap="round"/>
</svg>

<section>
  <div class="abs hero" role="img" aria-label="Foto: Burg über grünen Hängen der Steiermark"></div>
  <h1 class="abs hero-title script">Lorem Ipsum dolor</h1>
  <p class="abs hero-sub">ipsum dolor sit amet</p>
  <a class="abs hero-btn">Lorem Ipsum</a>
</section>

<section>
  <div class="abs welcome"></div>
  <div class="abs welcome-art" role="img" aria-label="Foto: Getreideähren und Hopfendolden auf weißem Holz"></div>
  <h2 class="abs welcome-title script">Herzlich Willkommen</h2>
  <div class="abs welcome-text">
    <p>Wir lieben die Steiermark mit ihrem guten Essen, hervorragendem Bier und exquisitem Wein und möchten gerne anspruchsvolle Gäste verwöhnen. Als Start-up Unternehmen mit Sitz in Berlin und wollen wir unsere Begeisterung für die Steiermark mit ihren kulinarischen Spezialitäten, wunderschönen Landschaften und gastfreundlichen Menschen gern mit unseren Gästen teilen.<br>„Gaumenwege“ ist daher auf der Suche nach Partnern, die mit uns unser neues Projekt in der Steiermark starten möchten.</p>
    <p>Unser Ziel ist es, exklusive Klein-gruppenreisen mit kulinarischem Schwerpunkt in die Steiermark zu führen. Wir konzentrieren uns auf Geschäftsleute aus Berlin und Brandenburg, die unsere Reisen als Marketinginstrument für Kunden, im Rahmen der Wertschätzung von Mitarbeitern oder auch einfach nur privat nutzen möchten.</p>
  </div>
  <a class="abs more-btn script">mehr lesen</a>
</section>

<section>
  <div class="abs offers"></div>
  <div class="abs feature" role="img" aria-label="Foto: Weinglas auf Holztisch im Weingarten mit Trauben und Walnüssen"></div>
  <h3 class="abs feature-title script">Lorem Ipsum</h3>
  <p class="abs feature-sub">Finden Sie Ihr Geschmackserlebnis<br>in der Steiermark!</p>
  <a class="abs feature-btn">Alle ansehen</a>

  <div class="abs card-img img-vine" style="left:543px" role="img" aria-label="Foto: Weintrauben am Rebstock vor Weinbergen"></div>
  <div class="abs card-img img-town" style="left:731px" role="img" aria-label="Foto: Historische Häuserfront in Graz mit Uhrturm"></div>
  <div class="abs card-img img-lake" style="left:918px" role="img" aria-label="Foto: Bergsee mit klarem Wasser vor Felswand"></div>

  <h4 class="abs card-title script" style="left:543px">Von Bier zu Wein</h4>
  <h4 class="abs card-title script" style="left:731px">Lorem Ipsum dolor</h4>
  <h4 class="abs card-title script" style="left:918px">Lorem Ipsum dolor</h4>
  <p class="abs card-text" style="left:543px">Lorem ipsum dolor sit amet,<br>consetetur sadipscing elitr</p>
  <p class="abs card-text" style="left:731px">Lorem ipsum dolor sit amet,<br>consetetur sadipscing elitr</p>
  <p class="abs card-text" style="left:918px">Lorem ipsum dolor sit amet,<br>consetetur sadipscing elitr</p>
  <p class="abs card-price" style="left:543px">199,00 - 249,00 €</p>
  <p class="abs card-price" style="left:731px">199,00 - 249,00 €</p>
  <p class="abs card-price" style="left:918px">199,00 - 249,00 €</p>
  <a class="abs card-btn" style="left:543px">jetzt buchen</a>
  <a class="abs card-btn" style="left:731px">jetzt buchen</a>
  <a class="abs card-btn" style="left:918px">jetzt buchen</a>

  <svg class="abs arrow" style="left:542px" width="12" height="20" viewBox="0 0 12 20"><polyline points="10,2 2,10 10,18" fill="none" stroke="#111" stroke-width="2"/></svg>
  <span class="abs slider-dot on" style="left:595px"></span>
  <span class="abs slider-dot" style="left:657px"></span>
  <span class="abs slider-dot" style="left:720px"></span>
  <span class="abs slider-dot" style="left:782px"></span>
  <span class="abs slider-dot" style="left:845px"></span>
  <span class="abs slider-dot" style="left:907px"></span>
  <span class="abs slider-dot" style="left:970px"></span>
  <span class="abs slider-dot" style="left:1032px"></span>
  <svg class="abs arrow" style="left:1084px" width="12" height="20" viewBox="0 0 12 20"><polyline points="2,2 10,10 2,18" fill="none" stroke="#111" stroke-width="2"/></svg>
</section>

<section>
  <div class="abs cta" role="img" aria-label="Foto: Weintrauben zwischen Weinblättern"></div>
  <h2 class="abs cta-title">Erleben Sie die<br>gastronomische Vielfalt der Süd-Steiermark</h2>
  <p class="abs cta-sub">Sie suchen ein bestimmtes Gaumenerlebnis?<br>Dann helfen wir Ihnen gerne weiter.</p>
  <a class="abs cta-btn">Jetzt beraten lassen</a>
</section>

<svg class="abs hills" viewBox="0 0 560 134" preserveAspectRatio="none" role="img" aria-label="Silhouette von Hügeln und Stadt">
  <path d="M0 134 L0 100 C60 60 120 20 200 8 C260 0 320 30 380 70 C440 105 500 110 560 134 Z" fill="var(--green)"/>
</svg>

<footer>
  <div class="abs footer"></div>
  <svg class="abs f-icon" style="top:2008px" width="11" height="15" viewBox="0 0 11 15"><path d="M5.5 0A5.5 5.5 0 0 0 0 5.5C0 9.5 5.5 15 5.5 15S11 9.5 11 5.5A5.5 5.5 0 0 0 5.5 0Z" fill="#fff"/><circle cx="5.5" cy="5.5" r="2" fill="var(--green)"/></svg>
  <p class="abs f-text f-name">Gaumenwege</p>
  <p class="abs f-text f-addr">Marlene Hofbauer<br>Lindenweg 12<br>D - 10437 Berlin</p>
  <svg class="abs f-icon" style="top:2077px" width="13" height="13" viewBox="0 0 13 13"><path d="M3 0L5 3 3.5 4.5C4.5 6.5 6.5 8.5 8.5 9.5L10 8 13 10 11 13C5 12 1 8 0 2Z" fill="#fff"/></svg>
  <p class="abs f-text f-phone">Deutschland: +49 170 2233 481<br>Österreich: +43 681 5522 9017</p>
  <div class="abs f-text f-col" style="left:461px"><strong>MENÜ</strong><br>MENÜPUNKT<br>MENÜPUNKT<br>MENÜPUNKT<br>MENÜPUNKT</div>
  <div class="abs f-text f-col" style="left:601px"><strong>MENÜ</strong><br>MENÜPUNKT<br>MENÜPUNKT<br>MENÜPUNKT<br>MENÜPUNKT</div>
  <span class="abs social" style="left:739px" aria-label="Soziales Netzwerk"></span>
  <span class="abs social" style="left:802px" aria-label="Videoportal"></span>
  <span class="abs social" style="left:865px" aria-label="Soziales Netzwerk"></span>
  <span class="abs social" style="left:927px" aria-label="Kurznachrichtendienst"></span>
  <div class="abs f-rule"></div>
  <p class="abs f-text copyright">© 2017. Agentur Kornfeld</p>
</footer>

</body>
</html>
```